International tourism and marketing agency needs 3 page glossy (digital) brochure

We need to update/design our sales brochure with updated events and vibrant images and videos. This needs to be a pdf with live links to images and videos. We are a social enterprise seeking to increase tourism in Kenya through our marketing company, catering to high net worth ($$) African-American professionals living in the USA.

Target Market(s)

Black Americans, High Net worth retired Americans

Industry/Entity Type

Tourism, Regional Marketing

Font styles to use
Sans Serif

Colors
00AB8E
00BBA5
67D7C9
C6EFE9
E9F9F6
EB3D1F
EC4F4E
F09395
F8D3D4
FCEDEE

Requirements
Must have
• Rich, bright colors, strong images that portray retreat, relaxation and KENYA
Nice to have
• A blend of smiling faces, animals from safari, beautiful beaches off the Indian Ocean,.Nice to have videos embedded in pdf for sharing digtitally.
Should not have
• boxy script. unprofessional images of partying or too many water images. Should not have a visual focus on non-Black Americans

```html
<!DOCTYPE html>
<html lang="en">
<head>
<meta charset="utf-8">
<title>Your Investment – Kenya Travel Brochure</title>
<link rel="stylesheet" href="https://fonts.googleapis.com/css2?family=Barlow:wght@400;500;600;700;800&family=Saira+Condensed:wght@600;700&display=swap">
<style>
:root{
  --backdrop:#2e2e2e;
  --paper:#ffffff;
  --green:#1f9e2a;
  --orange:#df6412;
  --amber:#f39a1b;
  --maroon:#6b1410;
  --deep-red:#6a120f;
  --ink:#222222;
  --yellow:#ffe600;
  --white:#ffffff;
}
*{margin:0;padding:0;box-sizing:border-box}
html,body{width:1200px;height:1177px;overflow:hidden;background:var(--backdrop)}
body{font-family:"Barlow",Arial,sans-serif;color:var(--ink)}
.page{position:absolute;left:240px;top:134px;width:726px;height:938px;background:var(--paper);overflow:hidden}
.abs{position:absolute}
.cond{font-family:"Saira Condensed","Arial Narrow",sans-serif}

.page-title{left:49px;top:8px;font-family:"Saira Condensed","Arial Narrow",sans-serif;font-weight:700;font-size:25px;color:var(--orange);letter-spacing:.2px}

.investment-band{left:0;top:49px;width:726px;height:102px;background:var(--green);color:var(--white)}
.investment-band p{position:absolute;font-weight:700;font-size:12.6px;line-height:16px}
.price-tag{position:absolute;left:350px;top:12px;height:30px;display:flex}
.price-label{background:var(--white);color:var(--ink);width:250px;font-weight:700;font-size:14px;line-height:30px;padding-left:9px}
.price-label small{font-size:11.5px}
.price-value{background:var(--deep-red);color:var(--white);width:68px;font-weight:800;font-size:15px;line-height:30px;text-align:center}

.entry-column{left:0;top:151px;width:232px;height:485px;background:var(--orange);color:var(--white)}
.entry-heading{position:absolute;left:43px;top:17px;width:176px;height:62px;background:var(--amber);border:2px solid var(--white);text-align:center;font-family:"Saira Condensed","Arial Narrow",sans-serif;font-weight:700;font-size:22px;line-height:24px;padding-top:6px}
.entry-list{position:absolute;left:44px;top:90px;width:180px;list-style:none}
.entry-list li{position:relative;padding-left:0;font-weight:700;font-size:11.6px;line-height:14.4px;margin-bottom:13px}
.entry-list li::before{content:"•";position:absolute;left:-9px}
.entry-list strong{color:var(--yellow)}
.entry-note{position:absolute;left:46px;top:427px;width:170px;font-style:italic;font-weight:700;font-size:11px;line-height:14px}

.facts{left:258px;top:166px;width:420px;font-size:11.6px;line-height:14.4px}
.facts dt{font-weight:800;text-transform:uppercase;letter-spacing:.3px}
.facts dd{margin:0}

.map-mark{left:528px;top:169px;width:154px;height:186px;background:var(--maroon);border-radius:38% 22% 30% 40% / 20% 26% 44% 38%;display:flex;align-items:center;justify-content:center;text-align:center;font-family:"Saira Condensed","Arial Narrow",sans-serif;font-weight:700;font-size:28px;line-height:31px;color:var(--white)}
.map-mark span{display:block}
.map-mark .hl{color:var(--amber)}

.video-button{left:256px;top:437px;width:356px;height:53px;background:linear-gradient(90deg,#e66c12,#ef8d1e);display:flex;align-items:center;padding-left:18px;color:var(--white);font-family:"Saira Condensed","Arial Narrow",sans-serif;font-weight:700;font-size:19px;letter-spacing:.4px}
.video-button svg{position:absolute;right:10px;top:8px}

.culture{left:258px;top:502px;width:430px;font-size:11.4px;line-height:14.2px}
.culture h3{font-weight:800;font-size:12px;color:var(--maroon);text-transform:uppercase}
.culture h3 span{color:var(--orange)}
.culture ul{list-style:none}
.culture li{position:relative;padding-left:10px}
.culture li::before{content:"•";position:absolute;left:0;color:var(--orange)}

.partner-band{left:0;top:636px;width:726px;height:241px;background:var(--maroon)}
.partner-tile{position:absolute;width:201px;height:102px;border:1.5px solid var(--white)}
.partner-tile .label{position:absolute;left:10px;top:6px;right:10px;height:18px;background:var(--white);border:1px solid var(--maroon);border-radius:3px;font-size:11px;font-weight:500;text-align:center;line-height:16px;color:var(--ink)}
.tile-resort{background:linear-gradient(160deg,#7fb7a0,#4c8c70 55%,#5fc3d4)}
.tile-suites{background:linear-gradient(160deg,#3b2a20,#8a6a52 60%,#d9cfc4)}
.tile-lounge{background:linear-gradient(160deg,#2a2414,#8a6a2a 50%,#c99c3e)}
.tile-house{background:linear-gradient(160deg,#e7d7c0,#6d8a4a 55%,#c24a2a)}
.tile-air{background:linear-gradient(180deg,#5a8fc7,#a6c7e6 60%,#d6e6f3)}
.tile-coast{background:linear-gradient(180deg,#9fc3e0,#dce8ef 55%,#b23246)}

.cta{left:0;top:877px;width:726px;height:61px;display:flex;align-items:center;justify-content:center;gap:10px}
.cta-text{font-family:"Saira Condensed","Arial Narrow",sans-serif;font-weight:700;font-size:31px;color:var(--maroon);letter-spacing:-.2px}
.cta-text span{color:var(--amber)}
</style>
</head>
<body>
<main class="page">
  <h1 class="abs page-title">YOUR INVESTMENT&nbsp; (In your SELF!)</h1>

  <section class="abs investment-band">
    <p style="left:49px;top:12px;width:300px">All interested travelers are welcome to pay<br>a lump sum or start a payment plan to pay for the</p>
    <div class="price-tag">
      <div class="price-label">PRIME TRAVEL PACKAGE <small>(Per Person)</small></div>
      <div class="price-value">$6,250</div>
    </div>
    <p style="left:49px;top:57px;width:640px">A Deposit (nonrefundable) of $1,000 must be received before a travel profile is created by KTRV/HOPE.<br>We have designed a simple payment plan for all guests.</p>
  </section>

  <aside class="abs entry-column">
    <h2 class="entry-heading">KENYA ENTRY<br>REQUIREMENT</h2>
    <ul class="entry-list">
      <li><strong>A valid US passport</strong> with at least two blank pages, 6 months' validity, and a visa are required to enter Kenya</li>
      <li><strong>Single-entry visas</strong> are available online and upon arrival at Kenyan airports; We will schedule time with you to apply for your Visa.</li>
      <li><strong>Proof of Yellow Fever Immunization</strong> - you may be denied entry without it. TravelWell Clinics has nationwide locations that provide the vaccine. (Trusted Provider: Dana Reed, MD at the Harbor Women's Care Center in Charleston, SC)</li>
      <li><strong>COVID vaccination card</strong> or (multiple) PCR test</li>
    </ul>
    <p class="entry-note">*You will be offered Travel &amp; Health Insurance by our trusted partner</p>
  </aside>

  <dl class="abs facts">
    <dt>Official Name:</dt><dd>Republic of Kenya</dd>
    <dt>Official Language(s):</dt><dd>English, Swahili (English is commonly spoken)</dd>
    <dt>Capitol:</dt><dd>Nairobi</dd>
    <dt>Location:</dt><dd>East Africa- Kenya borders Uganda,<br>South Sudan, Ethiopia, Somalia and Tanzania</dd>
    <dt>Currency:</dt><dd>Kenyan Shillings ($1USD= KSh124) We will take you to<br>exchange currency at the best rate while in Kenya</dd>
    <dt>Tipping:</dt><dd>Tipping varies on service you receive.<br>Tip around 10% in restaurants and 200-500 shillings for hotel staff</dd>
    <dt>Tourism:</dt><dd>Kenya has many national parks and wildlife reserves, with safaris featuring<br>large animals; lions, buffalo, leopards, elephants and rhinoceros</dd>
  </dl>

  <div class="abs map-mark" role="img" aria-label="Map outline of Kenya with the title Kenya Quick Facts">
    <div><span class="hl">KENYA</span><span>QUICK</span><span>FACTS</span></div>
  </div>

  <a class="abs video-button" href="#">DISCOVER KENYA VIDEO &amp; MOMBASA
    <svg width="36" height="36" viewBox="0 0 36 36" aria-hidden="true"><circle cx="18" cy="18" r="17" fill="#6a120f"/><path d="M14 10 L25 18 L14 26 Z" fill="#fff"/></svg>
  </a>

  <section class="abs culture">
    <h3>Culture Facts <span>(For better cultural awareness):</span></h3>
    <ul>
      <li>Kenyan Time is flexible. Culturally, the pace of life is slower.<br>Don't expect people to be in a rush the way Americans often are</li>
      <li>Tea is commonly served with every meal and during social gatherings</li>
      <li>Most public buildings will require you to enter through washing stations<br>ad security before entering any building/complex</li>
      <li>Kenyans value politeness and aren't rude or aggressive people.<br>Always greet people enthusiastically, smile, and be mindful to not be curt</li>
    </ul>
  </section>

  <section class="abs partner-band">
    <div class="partner-tile tile-resort" style="left:46px;top:14px" role="img" aria-label="Resort pool surrounded by palm trees"><div class="label">Coral Ridge Resort</div></div>
    <div class="partner-tile tile-suites" style="left:258px;top:14px" role="img" aria-label="Hotel suite bedroom with lamps"><div class="label">Savanna Suites</div></div>
    <div class="partner-tile tile-lounge" style="left:470px;top:14px" role="img" aria-label="Lounge with warm string lights under trees"><div class="label">Acacia Lounge</div></div>
    <div class="partner-tile tile-house" style="left:46px;top:126px" role="img" aria-label="Colourful restaurant interior with plants"><div class="label">Garden House Kenya</div></div>
    <div class="partner-tile tile-air" style="left:258px;top:126px" role="img" aria-label="Airliner flying above clouds"><div class="label">Safari Air</div></div>
    <div class="partner-tile tile-coast" style="left:470px;top:126px" role="img" aria-label="Patterned airliner parked on the runway"><div class="label">Coastline Airways</div></div>
  </section>

  <div class="abs cta">
    <svg width="32" height="32" viewBox="0 0 32 32" aria-hidden="true"><circle cx="16" cy="16" r="15" fill="#f39a1b"/><path d="M12.5 9 L22 16 L12.5 23 Z" fill="#fff"/></svg>
    <p class="cta-text">Reserve Your Dream Retreat <span>Today!</span></p>
  </div>
</main>
</body>
</html>
```